Talvix Inc

Hello.

I would like to take a wordpress ecomm template and turn it into a website that can display 100s of domain listings with short text box for description and a price .
One link to quorvend.example for immediate payment and with the confirmation/decline letter/email .
Five - six pages, Home, about us, domains, contact us, . Several columns or scrolling page for the domain page. I want to list several hundred virtual domains for sale .
Like a portfolio website but lists domain text .
This will be hosted on my server. On my domain.

Target Market(s)

End users, business owners, store front managers, online entpenauers , ect

Industry/Entity Type

Information Technology

Number of Pages Required

5+ page

Font styles to use
Sans Serif

Colors
0455a3
f78f20
abd036

Requirements
Must have
• Lots of white space, clean professional look . fast loading , use of greens and blues. Easy to read font.
• big headers , several - three different headers that rotate or move or clicks.
• A few current stock photos.
Should not have
• slow loading photos.
• More than two photos on any one page.

```html
<!DOCTYPE html>
<html lang="en">
<head>
<meta charset="utf-8">
<title>Talvix Inc — Domains for Sale</title>
<link rel="stylesheet" href="https://fonts.googleapis.com/css2?family=Source+Sans+3:wght@400;600;700;900&display=swap">
<style>
:root{
  --page:#e9e9e9;
  --navy:#050d2e;
  --blue:#0455a3;
  --blue-bright:#1a78d0;
  --orange:#f78f20;
  --ink:#333;
  --ink-soft:#555;
  --rule:#d2d2d2;
  --stripe:#f0f0f0;
  --head:#e2e2e2;
  --footer:#1c1c1c;
  --field:#353535;
  --white:#fff;
}
*{box-sizing:border-box;margin:0;padding:0}
html,body{width:1200px;height:2675px;overflow:hidden}
body{background:var(--page);font-family:"Source Sans 3",Arial,sans-serif;color:var(--ink);position:relative}

/* ---------- header / hero ---------- */
.hero{position:absolute;left:16px;top:18px;width:1170px;height:446px;overflow:hidden;
  background:radial-gradient(ellipse 60% 70% at 62% 30%,#1d3f8a 0%,#0b1f5c 40%,transparent 75%),
             radial-gradient(ellipse 40% 30% at 88% 95%,#4d8f8a 0%,transparent 70%),
             linear-gradient(180deg,#04092a 0%,#0a1a4d 55%,#0c2a5c 100%);
  box-shadow:0 14px 14px -8px rgba(0,0,0,.35)}
.topbar{position:absolute;right:0;top:0;width:553px;height:39px;background:var(--blue);
  clip-path:polygon(0 0,100% 0,100% 100%,5% 100%);display:flex;align-items:center;gap:30px;
  padding-left:62px;color:var(--white);font-weight:600;font-size:17px}
.topbar .item{display:flex;align-items:center;gap:9px}
.topbar svg{width:22px;height:22px}
.socials{display:flex;gap:4px}
.socials i{display:block;width:18px;height:18px;border:2px solid var(--white);border-radius:50%}
.logo{position:absolute;left:28px;top:30px;color:var(--white);font-weight:900;font-size:62px;letter-spacing:1px;line-height:1}
.nav{position:absolute;right:32px;top:82px;display:flex;align-items:center;gap:26px;color:var(--white);font-weight:700;font-size:16px}
.nav .active{border-bottom:3px solid var(--blue-bright);padding-bottom:6px;margin-top:9px}
.nav .cta{background:var(--blue);padding:8px 12px;border-radius:3px}
.search{position:absolute;left:284px;top:332px;width:600px;height:51px;border:2px solid var(--white);border-radius:4px;
  background:rgba(0,0,0,.35);display:flex;align-items:center;padding:0 10px}
.search svg{width:36px;height:36px}
.search .www{color:#dfe6f0;font-size:30px;font-weight:600;margin-left:16px;flex:1}
.search .btn{border:1px solid #bbb;background:#111;color:var(--white);font-weight:700;font-size:15px;padding:8px 18px;border-radius:2px}

/* ---------- listing ---------- */
.title{position:absolute;top:522px;left:0;width:1200px;text-align:center;color:var(--orange);font-weight:700;font-size:32px}
.listing{position:absolute;left:80px;top:606px;width:1040px;height:1669px;background:var(--white);border:1px solid var(--rule)}
.thead{display:grid;grid-template-columns:300px 460px 119px 130px 31px;height:48px;background:linear-gradient(#ececec,#dcdcdc);border-bottom:1px solid var(--rule)}
.thead div{display:flex;align-items:center;justify-content:center;gap:9px;color:var(--blue);font-weight:700;font-size:16px;border-right:1px solid var(--rule)}
.thead svg{width:20px;height:20px}
.thead .payname{font-size:22px;font-weight:700}
.rows{position:absolute;top:49px;left:0;width:1009px}
.row{display:grid;grid-template-columns:300px 460px 119px 130px;height:30px;font-size:14.5px;border-bottom:1px solid #e0e0e0}
.row:nth-child(even){background:var(--stripe)}
.row span{display:flex;align-items:center;padding-left:12px;border-right:1px solid var(--rule);white-space:nowrap;overflow:hidden}
.row span:nth-child(3){justify-content:center;padding:0}
.row span:nth-child(4){justify-content:center;padding:0}
.row i{display:block;width:11px;height:14px;background:var(--blue);border-radius:2px}
.scroll{position:absolute;right:0;top:49px;width:30px;height:1619px;background:#f6f6f6;border-left:1px solid var(--rule)}
.scroll .thumb{position:absolute;left:8px;top:22px;width:14px;height:266px;border:1px solid #bbb;border-radius:7px;background:#fafafa}
.scroll .up,.scroll .down{position:absolute;left:6px;width:0;height:0;border-left:9px solid transparent;border-right:9px solid transparent}
.scroll .up{top:6px;border-bottom:11px solid #222}
.scroll .down{bottom:6px;border-top:11px solid #222}

/* ---------- footer ---------- */
.footer{position:absolute;left:16px;top:2336px;width:1170px;height:289px;background:var(--footer);color:var(--white)}
.footer .logo{left:59px;top:118px;font-size:48px}
.about{position:absolute;left:417px;top:40px;width:265px}
.footer h3{font-size:17px;font-weight:700;margin-bottom:14px}
.about p{font-size:12.5px;line-height:17px;color:#8a8a8a}
.contact{position:absolute;left:802px;top:40px;width:307px}
.field{height:29px;background:var(--field);margin-bottom:6px;font-size:11px;color:#999;padding:6px 10px}
.field.msg{height:66px}
.submit{display:inline-block;background:var(--field);font-weight:700;font-size:14px;padding:5px 22px;margin-top:3px}
.bottombar{position:absolute;left:16px;top:2625px;width:1170px;height:32px;background:var(--blue);color:var(--white);
  display:flex;align-items:center;justify-content:space-between;padding:0 16px 0 32px;font-size:11px;font-weight:700}
.bottombar .socials i{width:22px;height:22px;background:var(--white);border:0}
</style>
</head>
<body>

<header class="hero" role="img" aria-label="Dark blue photo of glowing digital www lettering">
  <div class="topbar">
    <div class="item"><svg viewBox="0 0 24 24"><circle cx="12" cy="12" r="11" fill="none" stroke="#fff" stroke-width="2"/><path d="M8 6l2 0 1 3-1.5 1a7 7 0 0 0 3.5 3.5l1-1.5 3 1v2c0 1-1 1.5-2 1.5A9 9 0 0 1 6.5 8C6.5 7 7 6 8 6z" fill="#fff"/></svg>1-800-555-0142</div>
    <div class="item"><svg viewBox="0 0 24 24"><circle cx="12" cy="12" r="11" fill="none" stroke="#fff" stroke-width="2"/><rect x="6" y="8" width="12" height="8" fill="none" stroke="#fff" stroke-width="1.6"/><path d="M6 8l6 5 6-5" fill="none" stroke="#fff" stroke-width="1.6"/></svg>info@talvix.example</div>
    <div class="socials"><i></i><i></i><i></i></div>
  </div>
  <div class="logo">TALVIX</div>
  <nav class="nav">
    <span class="active">HOME</span><span>ABOUT US</span><span>DOMAINS</span><span>CONTACT</span><span class="cta">SEARCH DOMAIN</span>
  </nav>
  <div class="search">
    <svg viewBox="0 0 36 36"><circle cx="15" cy="15" r="10" fill="none" stroke="#ddd" stroke-width="4"/><path d="M22 22l10 10" stroke="#ddd" stroke-width="5" stroke-linecap="round"/></svg>
    <span class="www">www.</span>
    <span class="btn">SEARCH</span>
  </div>
</header>

<h1 class="title">DOMAINS FOR SALE</h1>

<section class="listing">
  <div class="thead">
    <div><svg viewBox="0 0 20 20"><circle cx="10" cy="10" r="9" fill="#0455a3"/><path d="M1 10h18M10 1c-4 4-4 14 0 18M10 1c4 4 4 14 0 18M3 5.5h14M3 14.5h14" stroke="#fff" stroke-width="1.2" fill="none"/></svg>DOMAIN NAME</div>
    <div><svg viewBox="0 0 20 20"><rect x="3" y="1" width="14" height="18" fill="none" stroke="#0455a3" stroke-width="1.6"/><path d="M6 6h8M6 9h8M6 12h8M6 15h5" stroke="#0455a3" stroke-width="1.4"/></svg>DESCRIPTIONS</div>
    <div><svg viewBox="0 0 20 20"><rect x="2" y="1" width="16" height="18" rx="2" fill="#0455a3"/><text x="10" y="15" font-size="13" font-weight="700" text-anchor="middle" fill="#fff" font-family="Source Sans 3, sans-serif">$</text></svg>PRICE</div>
    <div class="payname">Quorvend</div>
    <div></div>
  </div>
  <div class="rows">
    <div class="row"><span>abc.com</span><span>Lorem ipsum dolor sit amet, consectetuer adipiscing elit sed diam.</span><span>$2.99</span><span><i></i></span></div>
    <div class="row"><span>abca.com</span><span>Ut wisi enim ad minim veniam, quis nostrud exerci tation.</span><span>$3.99</span><span><i></i></span></div>
    <div class="row"><span>abccorp.com</span><span>Nam liber tempor cum soluta nobis eleifend option congue nihil.</span><span>$2.99</span><span><i></i></span></div>
    <div class="row"><span>abccompany.com</span><span>Typi non habent claritatem insitam; est usus legentis.</span><span>$2.99</span><span><i></i></span></div>
    <div class="row"><span>acquil.com</span><span>Claritas est etiam processus dynamicus, qui sequitur mutationem.</span><span>$4.99</span><span><i></i></span></div>
    <div class="row"><span>acquile.com</span><span>Lorem ipsum dolor sit amet, consectetuer adipiscing elit sed diam.</span><span>$5.99</span><span><i></i></span></div>
    <div class="row"><span>acquire.com</span><span>Ut wisi enim ad minim veniam, quis nostrud exerci tation.</span><span>$6.99</span><span><i></i></span></div>
    <div class="row"><span>acknowledge.com</span><span>Nam liber tempor cum soluta nobis eleifend option congue nihil.</span><span>$7.99</span><span><i></i></span></div>
    <div class="row"><span>act.com</span><span>Typi non habent claritatem insitam; est usus legentis.</span><span>$5.99</span><span><i></i></span></div>
    <div class="row"><span>actcorp.com</span><span>Claritas est etiam processus dynamicus, qui sequitur mutationem.</span><span>$2.99</span><span><i></i></span></div>
    <div class="row"><span>actcorporation.com</span><span>Lorem ipsum dolor sit amet, consectetuer adipiscing elit sed diam.</span><span>$3.99</span><span><i></i></span></div>
    <div class="row"><span>actingcorp.com</span><span>Ut wisi enim ad minim veniam, quis nostrud exerci tation.</span><span>$2.99</span><span><i></i></span></div>
    <div class="row"><span>admissions.com</span><span>Nam liber tempor cum soluta nobis eleifend option congue nihil.</span><span>$3.99</span><span><i></i></span></div>
    <div class="row"><span>autoart.com</span><span>Typi non habent claritatem insitam; est usus legentis.</span><span>$2.99</span><span><i></i></span></div>
    <div class="row"><span>autocare.com</span><span>Claritas est etiam processus dynamicus, qui sequitur mutationem.</span><span>$2.99</span><span><i></i></span></div>
    <div class="row"><span>autodealers.com</span><span>Lorem ipsum dolor sit amet, consectetuer adipiscing elit sed diam.</span><span>$4.99</span><span><i></i></span></div>
    <div class="row"><span>autodetails.com</span><span>Ut wisi enim ad minim veniam, quis nostrud exerci tation.</span><span>$5.99</span><span><i></i></span></div>
    <div class="row"><span>autonewyork.com</span><span>Nam liber tempor cum soluta nobis eleifend option congue nihil.</span><span>$6.99</span><span><i></i></span></div>
    <div class="row"><span>autony.com</span><span>Typi non habent claritatem insitam; est usus legentis.</span><span>$7.99</span><span><i></i></span></div>
    <div class="row"><span>autonj.com</span><span>Claritas est etiam processus dynamicus, qui sequitur mutationem.</span><span>$5.99</span><span><i></i></span></div>
    <div class="row"><span>autoshine.com</span><span>Lorem ipsum dolor sit amet, consectetuer adipiscing elit sed diam.</span><span>$2.99</span><span><i></i></span></div>
    <div class="row"><span>benn.com</span><span>Ut wisi enim ad minim veniam, quis nostrud exerci tation.</span><span>$3.99</span><span><i></i></span></div>
    <div class="row"><span>borgauto.com</span><span>Nam liber tempor cum soluta nobis eleifend option congue nihil.</span><span>$2.99</span><span><i></i></span></div>
    <div class="row"><span>bridesandgroomnewyork.com</span><span>Typi non habent claritatem insitam; est usus legentis.</span><span>$3.99</span><span><i></i></span></div>
    <div class="row"><span>bridesmaid.com</span><span>Claritas est etiam processus dynamicus, qui sequitur mutationem.</span><span>$2.99</span><span><i></i></span></div>
    <div class="row"><span>bronxauto.com</span><span>Lorem ipsum dolor sit amet, consectetuer adipiscing elit sed diam.</span><span>$2.99</span><span><i></i></span></div>
    <div class="row"><span>cardealers.com</span><span>Ut wisi enim ad minim veniam, quis nostrud exerci tation.</span><span>$4.99</span><span><i></i></span></div>
    <div class="row"><span>carforsale.com</span><span>Nam liber tempor cum soluta nobis eleifend option congue nihil.</span><span>$5.99</span><span><i></i></span></div>
    <div class="row"><span>carforrent.com</span><span>Typi non habent claritatem insitam; est usus legentis.</span><span>$6.99</span><span><i></i></span></div>
    <div class="row"><span>circlecenter.com</span><span>Claritas est etiam processus dynamicus, qui sequitur mutationem.</span><span>$7.99</span><span><i></i></span></div>
    <div class="row"><span>circledash.com</span><span>Lorem ipsum dolor sit amet, consectetuer adipiscing elit sed diam.</span><span>$5.99</span><span><i></i></span></div>
    <div class="row"><span>circlerestaurant.com</span><span>Ut wisi enim ad minim veniam, quis nostrud exerci tation.</span><span>$2.99</span><span><i></i></span></div>
    <div class="row"><span>corelink.com</span><span>Nam liber tempor cum soluta nobis eleifend option congue nihil.</span><span>$3.99</span><span><i></i></span></div>
    <div class="row"><span>corecorporation.com</span><span>Typi non habent claritatem insitam; est usus legentis.</span><span>$2.99</span><span><i></i></span></div>
    <div class="row"><span>corecircle.com</span><span>Claritas est etiam processus dynamicus, qui sequitur mutationem.</span><span>$3.99</span><span><i></i></span></div>
    <div class="row"><span>dashauto.com</span><span>Lorem ipsum dolor sit amet, consectetuer adipiscing elit sed diam.</span><span>$2.99</span><span><i></i></span></div>
    <div class="row"><span>drinkanddine.com</span><span>Ut wisi enim ad minim veniam, quis nostrud exerci tation.</span><span>$2.99</span><span><i></i></span></div>
    <div class="row"><span>delawareresto.com</span><span>Nam liber tempor cum soluta nobis eleifend option congue nihil.</span><span>$4.99</span><span><i></i></span></div>
    <div class="row"><span>denverauto.com</span><span>Typi non habent claritatem insitam; est usus legentis.</span><span>$5.99</span><span><i></i></span></div>
    <div class="row"><span>ebusiness.com</span><span>Claritas est etiam processus dynamicus, qui sequitur mutationem.</span><span>$6.99</span><span><i></i></span></div>
    <div class="row"><span>eshop.com</span><span>Lorem ipsum dolor sit amet, consectetuer adipiscing elit sed diam.</span><span>$7.99</span><span><i></i></span></div>
    <div class="row"><span>ecommerce.com</span><span>Ut wisi enim ad minim veniam, quis nostrud exerci tation.</span><span>$5.99</span><span><i></i></span></div>
    <div class="row"><span>friction.com</span><span>Nam liber tempor cum soluta nobis eleifend option congue nihil.</span><span>$2.99</span><span><i></i></span></div>
    <div class="row"><span>freightline.com</span><span>Typi non habent claritatem insitam; est usus legentis.</span><span>$3.99</span><span><i></i></span></div>
    <div class="row"><span>freightmaster.com</span><span>Claritas est etiam processus dynamicus, qui sequitur mutationem.</span><span>$2.99</span><span><i></i></span></div>
    <div class="row"><span>freightcompany.com</span><span>Lorem ipsum dolor sit amet, consectetuer adipiscing elit sed diam.</span><span>$3.99</span><span><i></i></span></div>
    <div class="row"><span>freightcorporation.com</span><span>Ut wisi enim ad minim veniam, quis nostrud exerci tation.</span><span>$2.99</span><span><i></i></span></div>
    <div class="row"><span>fusionrestaurant.com</span><span>Nam liber tempor cum soluta nobis eleifend option congue nihil.</span><span>$2.99</span><span><i></i></span></div>
    <div class="row"><span>fusionart.com</span><span>Typi non habent claritatem insitam; est usus legentis.</span><span>$4.99</span><span><i></i></span></div>
    <div class="row"><span>georgiaauto.com</span><span>Claritas est etiam processus dynamicus, qui sequitur mutationem.</span><span>$5.99</span><span><i></i></span></div>
    <div class="row"><span>georgiaproperty.com</span><span>Lorem ipsum dolor sit amet, consectetuer adipiscing elit sed diam.</span><span>$6.99</span><span><i></i></span></div>
    <div class="row"><span>globepartners.com</span><span>Ut wisi enim ad minim veniam, quis nostrud exerci tation.</span><span>$7.99</span><span><i></i></span></div>
    <div class="row"><span>globeseo.com</span><span>Nam liber tempor cum soluta nobis eleifend option congue nihil.</span><span>$5.99</span><span><i></i></span></div>
    <div class="row"><span>globeultimate.com</span><span>Typi non habent claritatem insitam; est usus legentis.</span><span>$2.99</span><span><i></i></span></div>
  </div>
  <div class="scroll"><div class="up"></div><div class="thumb"></div><div class="down"></div></div>
</section>

<footer class="footer">
  <div class="logo">TALVIX</div>
  <div class="about">
    <h3>ABOUT TALVIX, INC</h3>
    <p>Lorem ipsum dolor sit amet, consectetuer adipiscing elit, sed diam nonummy nibh euismod tincidunt ut laoreet dolore magna aliquam erat volutpat. Ut wisi enim ad minim veniam, quis nostrud exerci tation ullam corper suscipit lobortis nisl ut aliquip ex ea commodo consequat. Duis autem vel eum iriure dolor in hendrerit in vulputate velit esse molestie consequat, vel illum.</p>
  </div>
  <div class="contact">
    <h3>CONTACT US</h3>
    <div class="field">Name</div>
    <div class="field">Email</div>
    <div class="field msg">Message</div>
    <span class="submit">SUBMIT</span>
  </div>
</footer>
<div class="bottombar">
  <span>COPYRIGHT © 2016 TALVIX, INC. ALL RIGHTS RESERVED.</span>
  <div class="socials"><i></i><i></i><i></i></div>
</div>

</body>
</html>
```